ProLattice background/title banner

Feel free to visit my website (kvohomecheck.ca) and current NetLoop (KVO Property Inspections) page for a general feel. We focus on our trades background and experience. I have uploaded some logos that I would like used here. We offer Commercial, Residential, Agricultural inspections. With 24/7 online booking and call center.
Updates
Please ensure the small logos are added. Try to use all 3 colors. Red, Grey, Black (and some white), leave room for the profile pic that appear in the bottom left as well.
Target Market(s)
realtors and real estate professionals
Industry/Entity Type
Property Inspections for Real Estate
Logo Text
"Inspected by Tradesmen"
Font styles to use
Requirements
Must have
- To be simple with the key highlights and logos.

```html
<!DOCTYPE html>
<html lang="en">
<head>
<meta charset="utf-8">
<title>Residential &amp; Commercial Inspections – ProLattice Banner</title>
<link rel="stylesheet" href="https://fonts.googleapis.com/css2?family=Montserrat:wght@500;600;700&display=swap">
<style>
  :root {
    --red: #d1230d;
    --red-deep: #8c1e0c;
    --brown-dark: #3a1a12;
    --grey-bar: #333333;
    --white: #ffffff;
    --ink: #2a2a2a;
    --seal-red: #ee2a3b;
    --sky: #1a8fd6;
    --navy: #1d3a8a;
    --orange: #f28a1e;
  }
  * { margin: 0; padding: 0; box-sizing: border-box; }
  html, body { width: 1200px; height: 1200px; overflow: hidden; background: var(--white); }
  body { position: relative; font-family: "Montserrat", sans-serif; }

  .banner { position: absolute; left: 89px; width: 1044px; }
  .banner--photo { top: 409px; height: 177px; }
  .banner--flat { top: 671px; height: 176px; }

  .banner__field { position: absolute; left: 0; top: 0; width: 743px; height: 100%; }
  .banner--photo .banner__field {
    background: linear-gradient(115deg, var(--brown-dark) 0%, var(--red-deep) 35%, #b8321a 60%, var(--red-deep) 80%, #c2401f 100%);
  }
  .banner--flat .banner__field { background: var(--red); }

  .banner__bar { position: absolute; left: 743px; bottom: 0; width: 301px; height: 12px; background: var(--grey-bar); }
  .banner--flat .banner__bar { height: 11px; }

  .headline { position: absolute; width: 290px; text-align: center; color: var(--white); }
  .banner--photo .headline { left: 174px; top: 34px; }
  .banner--flat .headline { left: 159px; top: 31px; }
  .headline__mark { height: 48px; display: flex; align-items: center; justify-content: center; gap: 6px; font-size: 11px; font-weight: 600; letter-spacing: 0.4px; }
  .headline__mark-square { width: 9px; height: 9px; background: var(--white); flex: none; }
  .headline__kicker { font-size: 17.5px; font-weight: 500; letter-spacing: 0.3px; line-height: 1.2; }
  .headline__title { font-size: 40px; font-weight: 700; line-height: 1.05; letter-spacing: 0; }

  .services { position: absolute; list-style: none; color: var(--white); font-size: 11.5px; font-weight: 500; letter-spacing: 0.3px; line-height: 17px; }
  .banner--photo .services { left: 515px; top: 28px; }
  .banner--flat .services { left: 500px; top: 28px; }
  .services li { padding-left: 9px; position: relative; }
  .services li::before { content: "•"; position: absolute; left: 0; font-size: 8px; }
  .services li.services__more::before { content: ""; }

  .seal { position: absolute; border-radius: 50%; }
  .seal--ring { background: var(--white); width: 114px; height: 114px; left: 681px; top: 25px; }
  .seal--photo { background: var(--seal-red); width: 100px; height: 100px; left: 690px; top: 33px; }
  .seal--flat { background: var(--seal-red); width: 100px; height: 100px; left: 689px; top: 32px; }

  .partners { position: absolute; left: 820px; top: 0; width: 224px; height: 160px; }
  .partner { position: absolute; display: flex; align-items: center; gap: 5px; font-size: 11px; font-weight: 600; color: var(--ink); line-height: 1.15; white-space: nowrap; }
  .partner__dot { width: 14px; height: 14px; border-radius: 50%; flex: none; }
  .partner__dot--sky { background: var(--sky); }
  .partner__dot--navy { background: var(--navy); }
  .partner__square { width: 13px; height: 13px; background: var(--orange); flex: none; }
  .partner--sky { left: 8px; top: 48px; }
  .partner--hearth { left: 100px; top: 38px; font-size: 9.5px; white-space: normal; width: 80px; }
  .partner--therma { left: 2px; top: 116px; }
  .partner--ledger { left: 112px; top: 116px; }
</style>
</head>
<body>

<section class="banner banner--photo">
  <div class="banner__field" role="img" aria-label="Aerial photograph of suburban house rooftops with a red duotone tint"></div>
  <div class="banner__bar"></div>
  <div class="headline">
    <div class="headline__mark"><span class="headline__mark-square"></span>Inspected by Tradesmen</div>
    <div class="headline__kicker">RESIDENTIAL &amp; COMMERCIAL</div>
    <div class="headline__title">INSPECTIONS</div>
  </div>
  <ul class="services">
    <li>Property Inspections</li>
    <li>Mold &amp; Asbestos Testing</li>
    <li>Acreage Inspections</li>
    <li>Pre-Purchase Inspections</li>
    <li>Ozone/Odor Treatment</li>
    <li>HSTC Inspections</li>
    <li class="services__more">And More</li>
  </ul>
  <div class="seal seal--photo" role="img" aria-label="Trade certification seal"></div>
  <div class="partners">
    <div class="partner partner--sky"><span class="partner__dot partner__dot--sky"></span>SkyPoints</div>
    <div class="partner partner--hearth">Hearth Safety Technical Council</div>
    <div class="partner partner--therma"><span class="partner__dot partner__dot--navy"></span>ThermaView</div>
    <div class="partner partner--ledger"><span class="partner__square"></span>HouseLedger</div>
  </div>
</section>

<section class="banner banner--flat">
  <div class="banner__field"></div>
  <div class="banner__bar"></div>
  <div class="headline">
    <div class="headline__mark"><span class="headline__mark-square"></span>Inspected by Tradesmen</div>
    <div class="headline__kicker">RESIDENTIAL &amp; COMMERCIAL</div>
    <div class="headline__title">INSPECTIONS</div>
  </div>
  <ul class="services">
    <li>Property Inspections</li>
    <li>Mold &amp; Asbestos Testing</li>
    <li>Acreage Inspections</li>
    <li>Pre-Purchase Inspections</li>
    <li>Ozone/Odor Treatment</li>
    <li>HSTC Inspections</li>
    <li class="services__more">And More</li>
  </ul>
  <div class="seal seal--ring"></div>
  <div class="seal seal--flat" role="img" aria-label="Trade certification seal"></div>
  <div class="partners">
    <div class="partner partner--sky"><span class="partner__dot partner__dot--sky"></span>SkyPoints</div>
    <div class="partner partner--hearth">Hearth Safety Technical Council</div>
    <div class="partner partner--therma"><span class="partner__dot partner__dot--navy"></span>ThermaView</div>
    <div class="partner partner--ledger"><span class="partner__square"></span>HouseLedger</div>
  </div>
</section>

</body>
</html>
```